SHOP PAGE PRODUCT GRAPHICS 900x600 FOR E COMMERCE SITE. 5 TOTAL

NEED 5 GRAPHICS 900x600 MADE FOR MY SHOP PAGE HERE:

feel free to omit any redundant content http://plinkoridge.com/qx/darel/shop.jpg Custom Image For Products On Shop Page:AL A CARTE:Buy Video Ads On an As Needed Basis$37 PER VIDEO!INCLUDES:1 Video Ad ($149 VALUE) 1 Video Ad Converted To Square Ratio ($39 VALUE)1 Video Ad Converted To Vertical Ratio ($39 VALUE)1 Video Ad Converted To Pinwheeler Cover Video ($129 VALUE)VALUE $3564 Videos NOW ONLY $14960% OFF$37 PER VIDEO!INSTRUCTIONS FOR IMAGE:SHOW PHOTOS OF ALL PHOTOS SIZES USING SAME VIDEO. LET ME KNOW IF YOU NEED ONE I HAVE MP4 FILES FOR ALL SIZES SHOW PHOTOS OF ALL PHOTOS SIZES USING SAME VIDEO. LET ME KNOW IF YOU NEED ONE I HAVE MP4 FILES FOR ALL SIZES OR YOU CAN USE IMAGES FROM MY WEBSITE WWW.QUILLNESTFILMWORKS.COM PLEASE SCROLL DOWN ON HOMEPAGE AND SEE “VIDEO SIZES” SECTION AND USE THESE IMAGES IF YOU HAVE TO….I WANT THE IMAGE TO SHOW ALL THE DIFFERENT VIDEO SIZES THEY GET SO IT LOOKS LIKE A LOT OF VALUE…._______________________________________________________________________________________SUBSCRIPTION:Big Discounts Per Video When You Sign Up For A Monthly Subscription$25 PER VIDEO!INCLUDES:1 Video Ad ($149 VALUE)1 Video Ad Converted To Square Ratio ($39 VALUE)1 Video Ad Converted To Vertical Ratio ($39 VALUE)1 Video Ad Converted To Pinwheeler Cover Video ($129 VALUE)VALUE $3564 Videos NOW ONLY $9975% OFF$25 PER VIDEO!INSTRUCTIONS FOR IMAGE:SHOW PHOTOS OF ALL PHOTOS SIZES USING SAME VIDEO. LET ME KNOW IF YOU NEED ONE I HAVE MP4 FILES FOR ALL SIZES SHOW PHOTOS OF ALL PHOTOS SIZES USING SAME VIDEO. LET ME KNOW IF YOU NEED ONE I HAVE MP4 FILES FOR ALL SIZES OR YOU CAN USE IMAGES FROM MY WEBSITE WWW.QUILLNESTFILMWORKS.COM PLEASE SCROLL DOWN ON HOMEPAGE AND SEE “VIDEO SIEZES” SECTION AND USE THESE IMAGES IF YOU HAVE TO….I WANT THE IMAGE TO SHOW ALL THE DIFFERENT VIDEO SIZES THEY GET SO IT LOOKS LIKE A LOT OF VALUE….___________________________________________________________________________QUILLNEST MONTHLY CONTENT CALENDAR SUBSCRIPTION:Daily Content and Custom Branded Videos For Every Day.LESS THAN $10 PER VIDEO!INCLUDES:30 Videos ($1470 VALUE)VALUE $1470/mth30 Videos & Daily Content Only $299/mth90% OFF$10 PER VIDEO!INSTRUCTIONS FOR IMAGE:SHOW A PIC OF A CALENDAR WITH CONTENT/TEXT AND VIDEO FOR EACH DAY. SEE MY WEBSITE AT https://quillnestfilmworks.com/calendar/june and use something from here for this image. I WANT IT TO BE CLEAR THAT THEY WILL RECEIVE A VIDEO FOR EVERY DAY AND CONTENT TO POST TO THEIR SOCIAL MEDIA PAGES ______________________________________________________________________________HOLIDAY THEMED PACKAGECelebrate the Holidays with videos$58 PER VIDEO!INCLUDES:17 HOLIDAY THEMED VIDEOS ($1683 VALUE)VALUE $168317 Videos Only $99935% OFF$58 PER VIDEO!INSTRUCTIONS FOR IMAGE:SHOW A COLLAGE OF HOLIDAY THEMED VIDEOS. YOU CAN FIND SOME HOLIDAY THEMED VIDEOS ON MY WEBSITE HERE: https://quillnestfilmworks.com/categories FROM DROP DOWN MENU CHOOSE LABOR DAY, MEMORIAL DAY, HALLOWEEN, CHRISTMAS, NEW YEARS, NEW YEARS, VALENTINES TO SEE EXAMPLES OF HOLIDAY THEMED VIDEOS FOR THIS IMAGE. __________________________________________________________________SEASONAL THEMED PACKAGEWelcome every season with a new video$74 PER VIDEO!4 Seasonal Themed Videos ($396 VALUE)VALUE $3964 Videos Only $29925% OFF$74 PER VIDEO!INSTRUCTIONS FOR IMAGE:SHOW A COLLAGE OF SEASONAL THEMED VIDEOS. YOU CAN FIND THE SEASONAL THEMED VIDEOS ON MY WEBSITE FRAMLY PAGE HERE: https://framly.com/user51268403 SUMMER, SPRING, FALL, WINTER

Target Market(s)

B2B

Industry/Entity Type

Video Production

Colors

Designer to choose colors to be used in the design.

Requirements
Must have
• NEED 5 GRAPHICS MADE FOR MY SHOP PAGE HERE: 900x600 ://plinkoridge.com/qx/darel/shop.jpg
• Custom Image For Products On Shop Page:
• AL A CARTE:
• Buy Video Ads On an As Needed Basis
• $37 PER VIDEO!
• INCLUDES:
• 1 Video Ad ($149 VALUE)
• 1 Video Ad Converted To Square Ratio ($39 VALUE)
• 1 Video Ad Converted To Vertical Ratio ($39 VALUE)
• 1 Video Ad Converted To Pinwheeler Cover Video ($129 VALUE)
• VALUE $356
• 4 Videos NOW ONLY $149
• 60% OFF
• $37 PER VIDEO!
• INSTRUCTIONS FOR IMAGE:
• SHOW PHOTOS OF ALL PHOTOS SIZES USING SAME VIDEO. LET ME KNOW IF YOU NEED ONE I HAVE MP4 FILES FOR ALL SIZES SHOW PHOTOS OF ALL PHOTOS SIZES USING SAME VIDEO. LET ME KNOW IF YOU NEED ONE I HAVE MP4 FILES FOR ALL SIZES OR YOU CAN USE IMAGES FROM MY WEBSITE WWW.QUILLNESTFILMWORKS.COM PLEASE SCROLL DOWN ON HOMEPAGE AND SEE “VIDEO SIZES” SECTION AND USE THESE IMAGES IF YOU HAVE TO….I WANT THE IMAGE TO SHOW ALL THE DIFFERENT VIDEO SIZES THEY GET SO IT LOOKS LIKE A LOT OF VALUE….
• _______________________________________________________________________________________
• SUBSCRIPTION:
• Big Discounts Per Video When You Sign Up For A Monthly Subscription
• $25 PER VIDEO!
• INCLUDES:
• 1 Video Ad ($149 VALUE)
• VALUE $356
• 4 Videos NOW ONLY $99
• 75% OFF
• $25 PER VIDEO!
• INSTRUCTIONS FOR IMAGE:
• SHOW PHOTOS OF ALL PHOTOS SIZES USING SAME VIDEO. LET ME KNOW IF YOU NEED ONE I HAVE MP4 FILES FOR ALL SIZES SHOW PHOTOS OF ALL PHOTOS SIZES USING SAME VIDEO. LET ME KNOW IF YOU NEED ONE I HAVE MP4 FILES FOR ALL SIZES OR YOU CAN USE IMAGES FROM MY WEBSITE WWW.QUILLNESTFILMWORKS.COM PLEASE SCROLL DOWN ON HOMEPAGE AND SEE “VIDEO SIEZES” SECTION AND USE THESE IMAGES IF YOU HAVE TO….I WANT THE IMAGE TO SHOW ALL THE DIFFERENT VIDEO SIZES THEY GET SO IT LOOKS LIKE A LOT OF VALUE….
• ___________________________________________________________________________
• QUILLNEST MONTHLY CONTENT CALENDAR SUBSCRIPTION:
• Daily Content and Custom Branded Videos For Every Day.
• LESS THAN $10 PER VIDEO!
• INCLUDES:
• 30 Videos ($1470 VALUE)
• VALUE $1470/mth
• 30 Videos & Daily Content Only $299/mth
• 90% OFF
• $10 PER VIDEO!
• INSTRUCTIONS FOR IMAGE:
• SHOW A PIC OF A CALENDAR WITH CONTENT/TEXT AND VIDEO FOR EACH DAY. SEE MY WEBSITE AT https://quillnestfilmworks.com/calendar/june and use something from here for this image. I WANT IT TO BE CLEAR THAT THEY WILL RECEIVE A VIDEO FOR EVERY DAY AND CONTENT TO POST TO THEIR SOCIAL MEDIA PAGES
• ______________________________________________________________________________
• HOLIDAY THEMED PACKAGE
• Celebrate the Holidays with videos
• $58 PER VIDEO!
• INCLUDES:
• 17 HOLIDAY THEMED VIDEOS ($1683 VALUE)
• VALUE $1683
• 17 Videos Only $999
• 35% OFF
• $58 PER VIDEO!
• INSTRUCTIONS FOR IMAGE:
• SHOW A COLLAGE OF HOLIDAY THEMED VIDEOS. YOU CAN FIND SOME HOLIDAY THEMED VIDEOS ON MY WEBSITE HERE: https://quillnestfilmworks.com/categories FROM DROP DOWN MENU CHOOSE LABOR DAY, MEMORIAL DAY, HALLOWEEN, CHRISTMAS, NEW YEARS, NEW YEARS, VALENTINES TO SEE EXAMPLES OF HOLIDAY THEMED VIDEOS FOR THIS IMAGE.
• __________________________________________________________________
• SEASONAL THEMED PACKAGE
• Welcome every season with a new video
• $74 PER VIDEO!
• 4 Seasonal Themed Videos ($396 VALUE)
• VALUE $396
• 4 Videos Only $299
• 25% OFF
• $74 PER VIDEO!
• INSTRUCTIONS FOR IMAGE:
• SHOW A COLLAGE OF SEASONAL THEMED VIDEOS. YOU CAN FIND THE SEASONAL THEMED VIDEOS ON MY WEBSITE FRAMLY PAGE HERE: https://framly.com/user51268403 SUMMER, SPRING, FALL, WINTER
Nice to have
• NEED 5 GRAPHICS MADE FOR MY SHOP PAGE HERE: http://plinkoridge.com/qx/darel/shop.jpg 900x600
• AL A CARTE:
• $37 PER VIDEO!
• INCLUDES:
• 1 Video Ad ($149 VALUE)
• VALUE $356
• 4 Videos NOW ONLY $149
• 60% OFF
• $37 PER VIDEO!
• INSTRUCTIONS FOR IMAGE:
• SUBSCRIPTION:
• $25 PER VIDEO!
• INCLUDES:
• 1 Video Ad ($149 VALUE)
• VALUE $356
• 4 Videos NOW ONLY $99
• 75% OFF
• $25 PER VIDEO!
• INSTRUCTIONS FOR IMAGE:
• INCLUDES:
• 30 Videos ($1470 VALUE)
• VALUE $1470/mth
• 90% OFF
• $10 PER VIDEO!
• INSTRUCTIONS FOR IMAGE:
• HOLIDAY THEMED PACKAGE
• $58 PER VIDEO!
• INCLUDES:
• VALUE $1683
• 17 Videos Only $999
• 35% OFF
• $58 PER VIDEO!
• INSTRUCTIONS FOR IMAGE:
• SEASONAL THEMED PACKAGE
• $74 PER VIDEO!
• VALUE $396
• 4 Videos Only $299
• 25% OFF
• $74 PER VIDEO!
• INSTRUCTIONS FOR IMAGE:
Should not have
• AL A CARTE:
• $37 PER VIDEO!
• INCLUDES:
• 1 Video Ad ($149 VALUE)
• VALUE $356
• 4 Videos NOW ONLY $149
• 60% OFF
• $37 PER VIDEO!
• INSTRUCTIONS FOR IMAGE:
• SUBSCRIPTION:
• $25 PER VIDEO!
• INCLUDES:
• 1 Video Ad ($149 VALUE)
• VALUE $356
• 4 Videos NOW ONLY $99
• 75% OFF
• $25 PER VIDEO!
• INSTRUCTIONS FOR IMAGE:
• INCLUDES:
• 30 Videos ($1470 VALUE)
• VALUE $1470/mth
• 90% OFF
• $10 PER VIDEO!
• INSTRUCTIONS FOR IMAGE:
• HOLIDAY THEMED PACKAGE
• $58 PER VIDEO!
• INCLUDES:
• VALUE $1683
• 17 Videos Only $999
• 35% OFF
• $58 PER VIDEO!
• INSTRUCTIONS FOR IMAGE:
• SEASONAL THEMED PACKAGE
• $74 PER VIDEO!
• VALUE $396
• 4 Videos Only $299
• 25% OFF
• $74 PER VIDEO!
• INSTRUCTIONS FOR IMAGE:

```html
<!DOCTYPE html>
<html lang="en">
<head>
<meta charset="utf-8">
<title>Al a Carte – Shop Product Graphic</title>
<link href="https://fonts.googleapis.com/css2?family=Lato:wght@900&family=Montserrat:wght@500;600;700;800&display=swap" rel="stylesheet">
<style>
  :root {
    --stage: #c4c4c4;
    --banner: #e00000;
    --white: #ffffff;
    --ink: #1d1d1d;
    --ink-soft: #3c3c3c;
    --muted: #6a6a6a;
    --night: #0f1414;
    --sky: #08aeea;
    --sale-red: #ff3b3b;
    --sun: #fff500;
  }
  * { box-sizing: border-box; margin: 0; padding: 0; }
  html, body { width: 1200px; height: 1000px; overflow: hidden; }
  body {
    background: var(--stage);
    font-family: "Montserrat", Arial, sans-serif;
    position: relative;
  }
  .status-banner {
    position: absolute; left: 0; top: 44px; width: 1200px; height: 64px;
    background: var(--banner); color: var(--white);
    font-family: "Lato", Arial, sans-serif; font-weight: 900;
    font-size: 36px; letter-spacing: 0.5px;
    display: flex; align-items: center; justify-content: center;
  }
  .product-card {
    position: absolute; left: 146px; top: 243px; width: 940px; height: 627px;
    background: var(--white); overflow: hidden;
    box-shadow: 0 2px 8px rgba(0,0,0,0.35);
  }
  .dark-panel { position: absolute; inset: 0; }
  .package-title {
    position: absolute; left: 50px; top: 46px;
    font-size: 46px; font-weight: 800; color: var(--ink-soft);
    filter: blur(1.6px); letter-spacing: 0.5px;
  }
  .package-tagline {
    position: absolute; left: 48px; top: 99px;
    font-size: 17.5px; font-weight: 700; color: var(--ink-soft);
    filter: blur(0.6px);
  }
  .includes {
    position: absolute; left: 48px; top: 140px;
    font-size: 14.5px; font-weight: 500; color: var(--ink);
    line-height: 26px; list-style: none;
  }
  .includes-heading { font-weight: 600; }
  .price-tag {
    position: absolute; left: 48px; top: 311px; width: 130px; height: 65px;
    background: var(--sky); border-radius: 5px; color: var(--white);
    display: flex; align-items: center; justify-content: center; gap: 4px;
  }
  .price-currency { font-size: 30px; font-weight: 700; align-self: flex-start; margin-top: 8px; }
  .price-amount { font-size: 56px; font-weight: 800; line-height: 1; }
  .price-unit {
    position: absolute; left: 189px; top: 314px;
    font-size: 30px; font-weight: 800; color: var(--sky);
  }
  .price-value {
    position: absolute; left: 190px; top: 352px;
    font-size: 19px; font-weight: 500; color: var(--muted);
  }
  .price-value s { text-decoration-thickness: 1.5px; }
  .bundle-offer {
    position: absolute; left: 61px; top: 476px;
    font-size: 28px; font-weight: 800; filter: blur(1.8px); line-height: 40px;
  }
  .bundle-count { color: var(--muted); }
  .bundle-price { color: var(--sale-red); }
  .discount-badge {
    position: absolute; left: 354px; top: 389px; width: 190px; height: 190px;
    border-radius: 50%; background: var(--sun); filter: blur(3px);
    display: flex; flex-direction: column; align-items: center; justify-content: center;
    color: #2a2a14; font-weight: 800; line-height: 0.9;
  }
  .discount-rate { font-size: 60px; }
  .discount-label { font-size: 44px; }
</style>
</head>
<body>
  <div class="status-banner">UPLOADING MY FULL ENTRY SHORTLY</div>

  <section class="product-card">
    <svg class="dark-panel" width="940" height="627" viewBox="0 0 940 627" aria-hidden="true">
      <polygon points="692,0 940,0 940,627 332,627" fill="var(--night)"/>
    </svg>

    <h1 class="package-title">AL A CARTE</h1>
    <p class="package-tagline">Buy Video Ads On an As Needed Basis</p>

    <ul class="includes">
      <li class="includes-heading">INCLUDES:</li>
      <li>1 Video Ad &nbsp;($149 VALUE)</li>
      <li>1 Video Ad Converted To Square Ratio &nbsp;($39 VALUE)</li>
      <li>1 Video Ad Converted To Vertical Ratio &nbsp;($39 VALUE)</li>
      <li>1 Video Ad Converted To Pinwheeler Cover Video &nbsp;($129 VALUE)</li>
    </ul>

    <div class="price-tag"><span class="price-currency">$</span><span class="price-amount">37</span></div>
    <div class="price-unit">PER VIDEO</div>
    <div class="price-value">VALUE <s>$356</s></div>

    <div class="bundle-offer">
      <div class="bundle-count">4 Videos</div>
      <div class="bundle-price">NOW ONLY $149</div>
    </div>

    <div class="discount-badge">
      <span class="discount-rate">60%</span>
      <span class="discount-label">OFF</span>
    </div>
  </section>
</body>
</html>
```